Personal training poster - 1200X900mm

Poster to promote my new personal training service at my gym. The poster will be printed and put into an aframe to be seen by people walking past my gym. It needs to be simple and eye catching with the text i have put in the must haves. The text and image should be the prominent parts of the design.

Target Market(s)

30-50 year old females

Industry/Entity Type

Fitness

Font styles to use
Sans Serif

Requirements
Must have
• my logo
• exercise graphic
• Must include the following text:
• Are you looking for a personal trainer? Our expert trainers can help you achieve you take your health and fitness back!
• Contact details:
• 1300452968
• info@brightmovegym.com.au
• Located under the Harbourview Club

```html
<!DOCTYPE html>
<html lang="en">
<head>
<meta charset="utf-8">
<title>Personal Trainer Poster</title>
<link href="https://fonts.googleapis.com/css2?family=Jost:wght@500;600;700&display=swap" rel="stylesheet">
<style>
  :root {
    --page-bg: #ececef;
    --poster-red: #b43a38;
    --headline-red: #c23137;
    --highlight-yellow: #d8e23a;
    --trainer-blue: #1f5da6;
    --question-blue: #1d3f78;
    --band-yellow: #f2e13a;
    --light-panel-top: #dcdde3;
    --light-panel-bottom: #eeeef1;
  }
  html, body {
    margin: 0;
    padding: 0;
    width: 1200px;
    height: 1200px;
    overflow: hidden;
    background: var(--page-bg);
  }
  .poster {
    position: absolute;
    left: 194px;
    top: 30px;
    width: 812px;
    height: 1140px;
    display: block;
    box-shadow: 0 4px 18px rgba(0,0,0,0.15);
  }
  .poster text {
    font-family: "Jost", "Futura", sans-serif;
  }
  .headline-lead { fill: var(--trainer-blue); font-weight: 600; font-size: 33px; }
  .headline-main { fill: var(--headline-red); font-weight: 600; font-size: 40px; }
  .headline-mark { fill: var(--question-blue); font-weight: 700; font-size: 68px; }
  .subline { fill: var(--trainer-blue); font-weight: 700; font-size: 17px; }
  .subline .accent { fill: var(--headline-red); }
  .contact-label { fill: var(--poster-red); font-weight: 700; font-size: 11px; }
  .contact-line { fill: var(--poster-red); font-weight: 500; font-size: 14.5px; }
  .contact-line .key { font-weight: 700; }
  .location { fill: var(--band-yellow); font-weight: 700; font-size: 14.5px; }
  .brand-name { fill: var(--trainer-blue); font-weight: 700; font-size: 10px; }
</style>
</head>
<body>
<svg class="poster" viewBox="0 0 540 758" xmlns="http://www.w3.org/2000/svg">
  <defs>
    <linearGradient id="photoTone" x1="0" y1="0" x2="0" y2="1">
      <stop offset="0" stop-color="#9a9aa0"/>
      <stop offset="0.3" stop-color="#6f6e73"/>
      <stop offset="0.55" stop-color="#3b3a3f"/>
      <stop offset="1" stop-color="#1f1f23"/>
    </linearGradient>
    <radialGradient id="photoWarmth" cx="0.2" cy="0.55" r="0.35">
      <stop offset="0" stop-color="#c9d58a" stop-opacity="0.55"/>
      <stop offset="1" stop-color="#c9d58a" stop-opacity="0"/>
    </radialGradient>
    <radialGradient id="photoRed" cx="0.6" cy="0.62" r="0.5">
      <stop offset="0" stop-color="#8e2c2a" stop-opacity="0.45"/>
      <stop offset="1" stop-color="#8e2c2a" stop-opacity="0"/>
    </radialGradient>
    <radialGradient id="photoCenter" cx="0.65" cy="0.35" r="0.3">
      <stop offset="0" stop-color="#b9a894" stop-opacity="0.5"/>
      <stop offset="1" stop-color="#b9a894" stop-opacity="0"/>
    </radialGradient>
    <linearGradient id="lightPanel" x1="0" y1="0" x2="1" y2="1">
      <stop offset="0" stop-color="var(--light-panel-top)"/>
      <stop offset="1" stop-color="var(--light-panel-bottom)"/>
    </linearGradient>
    <radialGradient id="panelGlow" cx="0.85" cy="0.75" r="0.3">
      <stop offset="0" stop-color="#c9d4e6" stop-opacity="0.7"/>
      <stop offset="1" stop-color="#c9d4e6" stop-opacity="0"/>
    </radialGradient>
  </defs>

  <rect class="poster-base" x="0" y="0" width="540" height="758" fill="url(#lightPanel)"/>
  <rect class="panel-glow" x="300" y="420" width="240" height="300" fill="url(#panelGlow)"/>

  <g class="hero-photo" role="img" aria-label="Photo of a personal trainer coaching a woman doing a suspension strap push-up in a gym">
    <polygon points="0,0 540,0 540,303 380,395 199,395 0,253" fill="url(#photoTone)"/>
    <polygon points="0,0 540,0 540,303 380,395 199,395 0,253" fill="url(#photoCenter)"/>
    <polygon points="0,0 540,0 540,303 380,395 199,395 0,253" fill="url(#photoWarmth)"/>
    <polygon points="0,0 540,0 540,303 380,395 199,395 0,253" fill="url(#photoRed)"/>
  </g>

  <polygon class="red-wedge" points="0,253 199,395 380,395 540,303 540,333 0,708" fill="var(--poster-red)"/>
  <polygon class="red-stripe" points="295,385 540,215 540,226 306,385" fill="var(--poster-red)"/>

  <polygon class="headline-box" points="70,413 487,360 489,458 72,518" fill="var(--highlight-yellow)"/>
  <text class="headline-lead" transform="translate(87,455) rotate(-7)" textLength="340" lengthAdjust="spacingAndGlyphs">Are you looking for a</text>
  <text class="headline-main" transform="translate(82,501) rotate(-7.3)" textLength="367" lengthAdjust="spacingAndGlyphs">PERSONAL TRAINER</text>
  <text class="headline-mark" transform="translate(447,452) rotate(-7)">?</text>

  <polygon class="subline-box" points="119,518 439,478 442,552 122,598" fill="var(--highlight-yellow)"/>
  <text class="subline" transform="translate(133,538) rotate(-8)" textLength="294" lengthAdjust="spacingAndGlyphs">Our <tspan class="accent">EXPERT TRAINERS</tspan> can help</text>
  <text class="subline" transform="translate(156,560) rotate(-8)" textLength="255" lengthAdjust="spacingAndGlyphs">you achieve you take your</text>
  <text class="subline" transform="translate(164,583) rotate(-8)" textLength="245" lengthAdjust="spacingAndGlyphs"><tspan class="accent">HEALTH</tspan> and <tspan class="accent">FITNESS</tspan> back</text>

  <text class="contact-label" x="98" y="670" textLength="98" lengthAdjust="spacingAndGlyphs">Contact Details</text>
  <text class="contact-line" x="98" y="690" textLength="137" lengthAdjust="spacingAndGlyphs"><tspan class="key">Call -</tspan>1300452968</text>
  <text class="contact-line" x="98" y="710" textLength="246" lengthAdjust="spacingAndGlyphs"><tspan class="key">Email -</tspan> info@brightmovegym.com.au</text>

  <g class="brand">
    <circle cx="470" cy="668" r="16" fill="var(--trainer-blue)"/>
    <text class="brand-name" x="470" y="700" text-anchor="middle">BrightMove Gym</text>
  </g>

  <rect class="footer-band" x="0" y="725" width="540" height="28" fill="var(--poster-red)"/>
  <text class="location" x="98" y="744" textLength="247" lengthAdjust="spacingAndGlyphs">Located under the Harbourview Club</text>
</svg>
</body>
</html>
```